Dr. Marissa Tevlin Medical/Chiropractic Business Card

Dr. Tevlin is a chiropractor and will require a business card that she uses every single day to book appointments on the back side of the card. Currently the office name goes by Dr. Marissa Tevlin. The chiropractic profession is based on the diagnosis and manipulative treatment of misalignments of the joints, especially those of the spinal column, which are held to cause other disorders by affecting the nerves, muscles, and organs. Dr. Marissa Tevlin is looking for a contemporary and minimalistic design.

Industry/Entity Type

Medical

Contact Information for Business Card

Name: Dr. Marissa Tevlin; Address: 748 Harcastle Rd South, London, ON N5R 2K7; Phone Number: 519.274.6193; Fax: 519.281.5046; email: marissa.tevlin@quorvamail.com

Requirements
Must have
• ability to write multiple appointments date/time on the back of card

```html
<!DOCTYPE html>
<html lang="en">
<head>
<meta charset="UTF-8">
<title>Dr. Marissa Tevlin — Chiropractor Business Card</title>
<link rel="stylesheet" href="https://fonts.googleapis.com/css2?family=Arimo:wght@400;700&family=Open+Sans:wght@300&display=swap">
<style>
  :root {
    --navy-deep: #0d0f3a;
    --navy: #24247a;
    --indigo: #3b3b9a;
    --lavender: #a9a9e0;
    --ink: #111;
    --paper: #ffffff;
    --backdrop: #e9e7e2;
    --rule: #333;
  }
  html, body {
    margin: 0;
    width: 1200px;
    height: 900px;
    overflow: hidden;
    background: var(--backdrop);
    font-family: "Arimo", Arial, sans-serif;
  }
  .canvas { position: relative; width: 1200px; height: 900px; }

  .card {
    position: absolute;
    background: var(--paper);
    overflow: hidden;
    box-shadow: 0 6px 18px rgba(0,0,0,.18);
  }

  /* Front */
  .card-front { left: 40px; top: 250px; width: 700px; height: 400px; }
  .front-art { position: absolute; inset: 0; width: 700px; height: 400px; }
  .identity { position: absolute; left: 30px; top: 168px; }
  .identity .name { color: var(--paper); font-weight: 700; font-size: 32px; line-height: 1.15; margin: 0; white-space: nowrap; }
  .identity .role { color: var(--lavender); font-family: "Open Sans", Arial, sans-serif; font-weight: 300; font-size: 26px; line-height: 1.2; margin: 2px 0 0; }

  .main-phone { position: absolute; left: 385px; top: 286px; display: flex; align-items: center; gap: 10px; font-size: 30px; line-height: 1; color: var(--ink); white-space: nowrap; }
  .main-phone svg { width: 24px; height: 24px; }
  .about { position: absolute; left: 372px; top: 332px; width: 310px; font-size: 10px; line-height: 1.32; color: var(--ink); margin: 0; }

  .contact { position: absolute; right: 22px; top: 24px; text-align: right; font-size: 12.5px; line-height: 1.45; color: var(--ink); }
  .contact p { margin: 0; white-space: nowrap; }
  .contact .gap { margin-top: 12px; }
  .contact .row { display: flex; justify-content: flex-end; align-items: center; gap: 7px; }
  .contact svg { width: 12px; height: 12px; }

  /* Back */
  .card-back { left: 800px; top: 150px; width: 350px; height: 600px; }
  .appt-tab {
    position: absolute; left: 0; top: 0; width: 290px; height: 56px;
    background: linear-gradient(90deg, var(--navy-deep), var(--indigo));
    border-top-right-radius: 22px;
    color: var(--paper); font-weight: 700; font-size: 20px; letter-spacing: .5px;
    display: flex; align-items: center; padding-left: 22px; box-sizing: border-box;
  }
  .labels { position: absolute; top: 78px; left: 22px; right: 22px; font-size: 14px; color: var(--ink); }
  .labels .time { position: absolute; left: 205px; top: -6px; }
  .labels .date { position: absolute; left: 0; top: 26px; }
  .slots { position: absolute; left: 22px; right: 22px; top: 100px; }
  .slot { position: relative; height: 40px; }
  .slot .d { position: absolute; left: 0; width: 180px; bottom: 0; border-bottom: 1.5px solid var(--rule); }
  .slot .t { position: absolute; left: 198px; right: 0; bottom: 8px; border-bottom: 1.5px solid var(--rule); }
  .slot:first-child .d { left: 46px; width: 134px; }
  .reschedule {
    position: absolute; left: 0; right: 0; bottom: 30px; margin: 0;
    text-align: center; color: var(--navy); font-weight: 700; font-size: 15px; line-height: 1.3;
  }
</style>
</head>
<body>
<main class="canvas">

  <section class="card card-front" aria-label="Business card front">
    <svg class="front-art" viewBox="0 0 700 400" aria-hidden="true">
      <defs>
        <linearGradient id="panelShade" x1="0" y1="1" x2="1" y2="0">
          <stop offset="0" stop-color="#0d0f3a"/>
          <stop offset="1" stop-color="#3b3b9a"/>
        </linearGradient>
        <linearGradient id="swooshShade" x1="0" y1="0" x2="1" y2="0">
          <stop offset="0" stop-color="#1a1a5a"/>
          <stop offset="1" stop-color="#3b3b9a"/>
        </linearGradient>
      </defs>
      <path d="M0 0 H475 C465 150 395 300 305 400 H0 Z" fill="url(#swooshShade)"/>
      <path d="M0 0 H452 C442 150 372 300 282 400 H0 Z" fill="#ffffff"/>
      <path d="M0 0 H440 C430 150 360 300 270 400 H0 Z" fill="url(#panelShade)"/>
    </svg>

    <div class="identity">
      <p class="name">Dr. Marissa Tevlin</p>
      <p class="role">Chiropractor</p>
    </div>

    <div class="contact">
      <p>748 Harcastle Rd. London</p>
      <p>ON N5R 2K7</p>
      <p class="row gap">519.281.5046
        <svg viewBox="0 0 16 16" aria-label="Fax"><rect x="1" y="6" width="14" height="8" rx="1" fill="#24247a"/><rect x="4" y="1" width="8" height="6" fill="#24247a"/><rect x="4" y="9" width="8" height="2" fill="#fff"/></svg>
      </p>
      <p class="row">marissa.tevlin@quorvamail.com
        <svg viewBox="0 0 16 16" aria-label="Email"><rect x="1" y="3" width="14" height="10" fill="#24247a"/><path d="M1 3 L8 9 L15 3" stroke="#fff" stroke-width="1.4" fill="none"/></svg>
      </p>
    </div>

    <div class="main-phone">
      <svg viewBox="0 0 24 24" aria-label="Phone"><path d="M3 9 Q12 2 21 9 L19 12 L16 10 V8 Q12 6 8 8 V10 L5 12 Z" fill="#24247a"/><rect x="6" y="12" width="12" height="9" rx="1.5" fill="#24247a"/><circle cx="12" cy="16.5" r="2" fill="#fff"/></svg>
      <span>519.274.6193</span>
    </div>
    <p class="about">The chiropractic profession is based on the diagnosis and manipulative treatment of misalignments of the joints, especially those of the spinal column, which are held to cause other disorders by affecting the nerves, muscles, and organs.</p>
  </section>

  <section class="card card-back" aria-label="Business card back">
    <div class="appt-tab">APPOINTMENTS</div>
    <div class="labels">
      <span class="time">Time :</span>
      <span class="date">Date :</span>
    </div>
    <div class="slots">
      <div class="slot"><span class="d"></span><span class="t"></span></div>
      <div class="slot"><span class="d"></span><span class="t"></span></div>
      <div class="slot"><span class="d"></span><span class="t"></span></div>
      <div class="slot"><span class="d"></span><span class="t"></span></div>
      <div class="slot"><span class="d"></span><span class="t"></span></div>
      <div class="slot"><span class="d"></span><span class="t"></span></div>
      <div class="slot"><span class="d"></span><span class="t"></span></div>
      <div class="slot"><span class="d"></span><span class="t"></span></div>
      <div class="slot"><span class="d"></span><span class="t"></span></div>
      <div class="slot"><span class="d"></span><span class="t"></span></div>
    </div>
    <p class="reschedule">If you are unable to make your appointment,<br>please call us to reschedule</p>
  </section>

</main>
</body>
</html>
```